Digital Imaging Website Design Project

This project is for 3 page designs - The main Home page design, department page design & content page design which will utilize most of the home page components.

Client Background - http://www.kelrofab.com

An almost Forty year old established printing company that has a large client base of architect/engineering, as the print shop opened up as a blueprinting company, and over the years has grown, changed and expanded to offer document and digital file management for this industry. KRFab. has also always offered color printing services, but recently has expanded their color department to be able to offer amazing dimensional printing, and extreme cutting technology.

These new products and services will be targeted to new industries for repeatable printing needs, promotional, point of purchase color printing, as well as in-store, interior decor/wall. These new printing services are only offered by KRFAB in their area, and they want to convey that they are on the leading edge of color printing technology, while at the same time, not eliminating their existing primary business scaring away their traditional client base of architectural/engineering firms that use them for large format printing, scanning and document management services.

1 - Home Page Design
Primary Goals of the design:

1.Provide a new, eye catching engaging website that conveys the above expansion/growth/cutting edge company.
2.Full screen design please to move away from the 'center' bordered up website they currently have.
3.Design Components – We don't have any media to provide you with exception of our logo. We're looking for fresh design that is exciting and engaging imagery. Additionally, we are working on a color/effected version of our logo to place on the color division page, and this will probably tie in with the design you create for us.
4.It should be designed to be able to work as a responsive design as well so that when installed, will work across devices etc..
5.Colors – Same color scheme, but if you have an accent color you'd like to use to make the site pop, go for it!

Requirements:
1.The 4 divisions of the company should be the main feature so that the client depending on which department they are needing, will see those 4 choices clearly in the design, and they'll know to click on one of them to get more information and to their needed services.

2.The main goal of the site is to get visitors to place an order, there should be a feature on the home page for this call to action.

3.Put in an element that communicates the main benefit of KRFab. - an area for a 1-line Statement/Call to Action / Overall Company Benefit/

4.The 4 divisions need to have eye catching elements related to their products and services, and that clearly illustrate that the user should click on that to go to the appropriate area for products and services

Reprographics
This department is specifically geared to architect/engineering industry
BYLine for optional Use: Partnering with Building Industry Providers since 1975
Related pages for better understanding:
http://www.kelrofab.com/services/portland_professional_printing_services
http://www.kelrofab.com/services/reprographics
Digital File Management
This department is related to Architect/engineers, but can also apply to any other industry needing electronic document management, scanning, or archival services.
BYLine for optional use: Effective & Efficient Digital Solutions at every level.
Related Pages:
http://www.kelrofab.com/colorgraphics/electronic_file_document_management
http://www.kelrofab.com/colorgraphics/document_scanning_service
http://www.kelrofab.com/services/scanning_and_archiving

Color Graphics
This Department is newly expanded / has expanded services / they are focusing more of their efforts on this department and is a key reason for updated website design.
This Department image/representation should be stellar in the imagery to convey the excellence of the color department the services availble.
One of their newest products/services is dimensional printing – not 3-D, but raised element printing. Essentially a client could pick components on their graphic that that they want to 'bump' out, and additional layers would be put in place to create a popped out, dimensional effect. * Bonus points for creating the color department image that effectively conveys this new service – whether it's showing an abstract image/element that is actually raised off the page/paper/component. Additionally the color dimensional printing can be done on practically any material – glass, vinyl, material etc.... Please let me know if you have any questions on this.
BYLine for optional Use: See How Our Color Stands Out From the Rest
Related pages:
http://www.kelrofab.com/colorgraphics
http://www.kelrofab.com/colorgraphics/color_digital_imaging

Equipment & Supplies
This department provides specific supplies and hardware vs. printing products/services. Our largest client base is architects/engineers, but is not limited to this industry. Typical equipment is large printers, and supplies are typically paper products geared to the large format printing services, for the architect/engineers industry.
Byline for optional Use: In-House Printing & Fulfillment Services
Related pages:
http://www.kelrofab.com/varlen_tusk_equipment_sales
http://www.kelrofab.com/supplies

Additionally - Possibly have descriptive text sections below these 4 elements, but this is optional.

2.) Department/Division Page design -

This page should pull the home page element to over based on which division is selected.
Have a submenu design incorporated so that users can navigate to all the products and services that will be listed under that division
Contain a plugin design for FAQs – so that depending on which division page they are on, the appropriate FAQ's would display for use to have easy access to.
Contain a plugin design for – Contact Us easy form – short form –
Name
Company
Number
Email
Project Details/Questions: Text box

3.)Content Page design
This page should have main area for content
Area for an image with slideshow of other supporting images
Optional area for video – most (99%) of the pages will not have videos, but in the case we do, would like an area that will display videos effectively.
Optional FAQ plugin display
Contact plugin display

Global Elements:

Static and very visible site features that are in a position so that if user clicks beyond home page will still see these are:
Get a Quote
Place Order
Digital Plan-room
Call Today - 503-481-7962

Other global components:
SM Icons – QN, Chirpo, WorkLoop
Rotating Testimonial

Navigational Menu:
The KRF Difference
About
Sustainability
Products & Services
Reprograhics
Digital File Management
Color Graphics
Equipment & Supplies
Login
Blog
Contact Us

After the contest – What would be great to have is when a user clicks on one of the departments, it takes that visual element and continues onto it's department page for a smaller but related image - But this may be an after this web design contest.

Additionally will need some other design work on the interior pages, as well, so hoping to find a great designer to complete the other tasks – as well as be the go-to for future endeavors!

Thanks for looking at the project, and I look forward to any questions you may have.
Updates

Looking forward to hearing from interested designers! - If you're curious about my work, you can find my profile at:  https://www.gigmarla.com/users/~07b3e2f95d18c4a260

Target Market(s)

Please see description

Industry/Entity Type

Electronic

Requirements
Must have
• Please see description

```html
<!DOCTYPE html>
<html lang="en">
<head>
<meta charset="utf-8">
<title>KRF Digital Imaging</title>
<link href="https://fonts.googleapis.com/css2?family=Open+Sans:ital,wght@0,400;0,600;0,700;1,400&display=swap" rel="stylesheet">
<style>
:root{
  --navy:#0d2a78;
  --navy-dark:#071d5c;
  --blue:#1a3f94;
  --blue-mid:#2352b0;
  --link:#1d3c9a;
  --orange:#f37b17;
  --orange-light:#ffa31a;
  --green:#74a514;
  --green-light:#95c423;
  --text:#4a4a4a;
  --grey-line:#d9dde6;
  --white:#ffffff;
}
*{margin:0;padding:0;box-sizing:border-box}
html,body{width:887px;height:1200px;overflow:hidden;background:var(--white)}
body{font-family:"Open Sans",Arial,sans-serif;color:var(--text)}
.page{position:relative;width:887px;height:1200px;overflow:hidden}
.abs{position:absolute}
a{color:inherit;text-decoration:none}

.top-strip{left:0;top:0;width:887px;height:4px;background:#c5cde0}

/* header */
.brand{left:50px;top:30px;display:flex;align-items:center;gap:10px}
.brand-mark{width:22px;height:22px;background:var(--navy)}
.brand-name{font-size:30px;font-weight:700;color:var(--navy);letter-spacing:1px}
.brand-full{left:184px;top:28px;font-size:13px;font-weight:700;color:var(--navy);line-height:14.5px;text-transform:uppercase}
.brand-tag{left:184px;top:78px;font-size:8.5px;font-style:italic;color:var(--navy)}
.call{left:446px;top:13px;font-size:13.5px;color:#333;display:flex;align-items:center;gap:4px;white-space:nowrap}
.call strong{font-size:16px;font-weight:700;color:var(--navy);margin-left:4px;letter-spacing:-.2px}
.util-links{left:658px;top:14px;font-size:10.5px;color:var(--link);white-space:nowrap}
.util-links span{margin:0 4px;color:#555}
.quick-btn{top:66px;height:27px;border:1px solid #b9bcc4;border-radius:2px;background:linear-gradient(#ffffff,#e6e7ea);display:flex;align-items:center;justify-content:center;gap:6px;font-size:11.5px;color:#222}
.quick-btn svg{width:16px;height:16px}

/* main nav */
.main-nav{left:0;top:103px;width:887px;height:42px;background:linear-gradient(#2f5cb9,#143b8f);display:flex}
.main-nav a{height:42px;line-height:42px;color:var(--white);font-size:14.5px;padding:0 19px;border-right:1px solid rgba(255,255,255,.25)}
.main-nav a:first-child{padding-left:55px}

/* hero */
.hero{left:0;top:145px;width:887px;height:300px;background:radial-gradient(ellipse at 70% 50%,#ffffff 0%,#f6f5f0 60%,#eeede6 100%)}
.hero-kicker{left:59px;top:195px;font-size:22px;color:var(--orange);font-weight:400}
.hero-title{left:58px;top:218px;font-size:38px;color:var(--orange);font-weight:700;letter-spacing:-.3px}
.hero-text{left:60px;top:270px;width:345px;font-size:12px;line-height:18px;color:#555}
.hero-btn{left:60px;top:315px;width:94px;height:31px;background:linear-gradient(#22408a,#0b205d);border-radius:3px;color:var(--white);font-size:11.5px;line-height:31px;text-align:center}
.hero-dots{left:61px;top:373px;display:flex;gap:2px}
.hero-dots i{width:10px;height:10px;border-radius:50%;background:#a9a9a9}
.hero-dots i.on{background:#111}
.hero-visual{left:404px;top:186px;width:438px;height:212px;border-radius:4px;background:linear-gradient(#c9cbd1 0%,#4b4e58 20%,#e8eaef 45%,#d8dbe2 80%,#8e9199 100%)}

/* divisions */
.divisions{left:0;top:446px;width:887px;height:170px;background:var(--blue)}
.division-strip{left:38px;top:458px;width:803px;height:98px}
.division{top:566px;white-space:nowrap}
.division h3{font-size:16px;font-weight:400;color:var(--white);letter-spacing:-.3px}
.division a{display:block;font-size:9.5px;color:var(--white);margin-top:1px;padding-left:1px}

/* content */
.rule{left:46px;top:674px;width:794px;height:1px;background:#e3e3e3}
.section-title{font-size:19px;font-weight:600;color:var(--navy-dark)}
.about-title{left:50px;top:696px}
.about-photo{left:47px;top:731px;width:101px;height:95px;border-radius:8px;background:linear-gradient(135deg,#8a8f96,#c9c2b8 50%,#e3584e 70%,#4fa0d8)}
.about-text{left:49px;top:730px;width:300px;font-size:10.4px;line-height:18.7px;color:var(--link)}
.about-text .float{float:left;width:110px;height:94px}
.read-more{left:50px;top:870px;width:68px;height:21px;background:linear-gradient(#22408a,#0b205d);border-radius:2px;color:var(--white);font-size:8px;line-height:21px;text-align:center}
.news-title{left:378px;top:698px}
.news{left:379px;top:731px;width:220px;font-size:10.3px;line-height:18.5px;color:#555}
.news p{margin-bottom:15px}
.news b{font-weight:600;color:#444}

.cta{left:637px;width:204px;border-radius:2px;color:var(--white);display:flex;gap:6px;padding:9px 0 0 12px;box-shadow:0 1px 2px rgba(0,0,0,.25)}
.cta svg{width:26px;height:26px;flex:none}
.cta strong{display:block;font-size:16px;font-weight:400;line-height:20px}
.cta small{display:block;font-size:8.5px;opacity:.8;margin-top:2px}
.cta-quote{top:690px;height:59px;background:linear-gradient(#2b56b3,#0f2f7c)}
.cta-order{top:754px;height:59px;background:linear-gradient(var(--orange-light),#f27a0d)}
.cta-plan{top:820px;height:65px;background:linear-gradient(var(--green-light),var(--green))}

/* footer */
.footer{left:0;top:929px;width:887px;height:271px;background:linear-gradient(#1f4ca6 0%,#163d93 50%,#0f2f80 100%)}
.foot-title{font-size:16px;font-weight:400;color:var(--white)}
.foot-col{top:956px}
.foot-col ul{list-style:none;margin-top:9px}
.foot-col li{font-size:10.4px;color:var(--white);line-height:22.6px}
.testimonials{left:368px;top:950px;width:234px;height:160px;border-radius:4px;background:linear-gradient(#2a55ad,#0c2a73);border:1px solid rgba(255,255,255,.15);box-shadow:0 2px 5px rgba(0,0,0,.3);padding:14px 18px 0 24px;color:var(--white)}
.testimonials h3{font-size:17px;font-weight:400}
.testimonials p{font-size:9.3px;font-style:italic;line-height:16px;margin-top:8px;opacity:.9}
.testimonials .author{font-size:10px;font-weight:600;margin-top:6px}
.testimonials svg{position:absolute;right:16px;bottom:13px}
.social{left:658px;top:986px;display:flex;gap:3px}
.social i{width:26px;height:26px;border-radius:50%;background:var(--white);border:2px solid #c9d3ea}
.social-names{left:659px;top:1017px;font-size:10.4px;color:var(--white)}
.foot-rule{left:70px;top:1152px;width:748px;height:1px;background:rgba(255,255,255,.2)}
.copyright{left:74px;top:1167px;font-size:10px;color:rgba(255,255,255,.45)}
</style>
</head>
<body>
<div class="page">
  <div class="abs top-strip"></div>

  <header>
    <div class="abs brand"><span class="brand-mark"></span><span class="brand-name">KRF</span></div>
    <div class="abs brand-full">Kelro Print &amp;<br>Fabrication<br>Co.</div>
    <div class="abs brand-tag">Client-Driven Service Since 1975</div>

    <div class="abs call">
      <svg width="16" height="12" viewBox="0 0 16 12"><path d="M1 4c4-4 10-4 14 0l-2 2-3-1V3H6v2L3 6z M4 6h8l2 5H2z" fill="#111"/></svg>
      Call Today <strong>503-481-7962</strong>
    </div>
    <nav class="abs util-links"><a>About</a><span>|</span><a>Login</a><span>|</span><a>Blog</a><span>|</span><a>Contact Us</a></nav>

    <a class="abs quick-btn" style="left:502px;width:100px">
      <svg viewBox="0 0 16 16"><path d="M2 3h12a1 1 0 0 1 1 1v5a1 1 0 0 1-1 1H7l-4 3v-3H2a1 1 0 0 1-1-1V4a1 1 0 0 1 1-1z" fill="none" stroke="#111" stroke-width="2"/></svg>Get a Quote</a>
    <a class="abs quick-btn" style="left:610px;width:100px">
      <svg viewBox="0 0 16 16"><path d="M1 2h3l2 8h8l1-6H5" fill="none" stroke="#111" stroke-width="1.5"/><circle cx="7" cy="13" r="1.4"/><circle cx="13" cy="13" r="1.4"/></svg>Place Order</a>
    <a class="abs quick-btn" style="left:718px;width:120px">
      <svg viewBox="0 0 16 16"><path d="M8 1l6 3.5v7L8 15l-6-3.5v-7z" fill="none" stroke="#333" stroke-width="1.4"/></svg>Digital Planroom</a>
  </header>

  <nav class="abs main-nav">
    <a>The KRF Difference</a><a>Products &amp; Services</a><a>Login</a><a>About</a><a>Contact Us</a>
  </nav>

  <section>
    <div class="abs hero"></div>
    <div class="abs hero-kicker">Nunc tempus felis vitae</div>
    <h1 class="abs hero-title">Digital Printing</h1>
    <p class="abs hero-text">Mauris vel lacus vitae felis vestibulum volutpat. Etiam est nunc, venenatis in, tristique eu, imperdiet ac, nisl.</p>
    <a class="abs hero-btn">VIEW MORE</a>
    <div class="abs hero-dots"><i class="on"></i><i></i><i></i><i></i></div>
    <div class="abs hero-visual" role="img" aria-label="Wide-format printer producing a colourful beverage poster"></div>
  </section>

  <section>
    <div class="abs divisions"></div>
    <svg class="abs division-strip" viewBox="0 0 803 98" role="img" aria-label="Four slanted division images: blueprint rolls, file management workstation, colour swatches, large-format printer">
      <defs>
        <linearGradient id="g-repro" x1="0" x2="1"><stop offset="0" stop-color="#e8eef6"/><stop offset="1" stop-color="#b8c6dc"/></linearGradient>
        <linearGradient id="g-file" x1="0" x2="1"><stop offset="0" stop-color="#3a6a9a"/><stop offset="1" stop-color="#c58b3a"/></linearGradient>
        <linearGradient id="g-color" x1="0" x2="1"><stop offset="0" stop-color="#2aa832"/><stop offset=".3" stop-color="#f2d21a"/><stop offset=".55" stop-color="#e8301e"/><stop offset=".8" stop-color="#c52cc8"/><stop offset="1" stop-color="#3f9fe0"/></linearGradient>
        <linearGradient id="g-equip" x1="0" x2="1"><stop offset="0" stop-color="#d8d9dc"/><stop offset="1" stop-color="#f4f4f5"/></linearGradient>
      </defs>
      <polygon points="58,0 242,0 192,98 0,98" fill="url(#g-repro)"/>
      <polygon points="242,0 430,0 378,98 192,98" fill="url(#g-file)"/>
      <polygon points="430,0 616,0 564,98 378,98" fill="url(#g-color)"/>
      <polygon points="616,0 803,0 752,98 564,98" fill="url(#g-equip)"/>
    </svg>
    <div class="abs division" style="left:38px"><h3>Reprographics</h3><a>MORE INFO</a></div>
    <div class="abs division" style="left:227px"><h3>Digital File Management</h3><a>MORE INFO</a></div>
    <div class="abs division" style="left:424px"><h3>Color Graphics</h3><a>MORE INFO</a></div>
    <div class="abs division" style="left:604px"><h3>Equipment &amp; Supplies</h3><a>MORE INFO</a></div>
  </section>

  <main>
    <div class="abs rule"></div>

    <h2 class="abs section-title about-title">About Our Company</h2>
    <div class="abs about-photo" role="img" aria-label="Hands checking colour print swatches"></div>
    <p class="abs about-text"><span class="float"></span>Founded in 1975 by Daniel Ferrow, Kelro Print &amp; Fabrication (KR&amp;F) is a full service reprographics company serving Oregon and Southwest Washington's design and building community. We utilize the latest digital technologies to provide a wide range of reprographics and graphic imaging</p>
    <a class="abs read-more">READ MORE</a>

    <h2 class="abs section-title news-title">Recent News</h2>
    <div class="abs news">
      <p><b>07/10/2013</b> Phasellus felis dolor, scelerisque a, tempus eget, lobortis id, libero.</p>
      <p><b>06/10/2013</b> Donec scelerisque leo ac risus.</p>
      <p><b>05/10/2013</b> Praesent sit amet est. In dictum, dolor eu dictum porttitor enim felis viverra</p>
    </div>

    <a class="abs cta cta-quote">
      <svg viewBox="0 0 26 26"><path d="M13 2C6 2 1 6.5 1 12s4 9 9 9.6L8 25l7-3.5C21 21 25 17 25 12S20 2 13 2z" fill="#fff"/><path d="M8 10h4v4l-2 3M14 10h4v4l-2 3" fill="none" stroke="#1d3f92" stroke-width="2"/></svg>
      <span><strong>Get a Quote</strong><small>Nunc tempus felis vitae urna</small></span></a>
    <a class="abs cta cta-order">
      <svg viewBox="0 0 26 26"><path d="M1 4h4l3 12h13l2-9H7" fill="none" stroke="#fff" stroke-width="2"/><circle cx="10" cy="21" r="2" fill="#fff"/><circle cx="19" cy="21" r="2" fill="#fff"/></svg>
      <span><strong>Place Order</strong><small>Vivamus porttitor g purus nisi</small></span></a>
    <a class="abs cta cta-plan" style="padding-top:12px">
      <svg viewBox="0 0 26 26"><circle cx="13" cy="13" r="11" fill="none" stroke="#fff" stroke-width="2"/><path d="M2 13h22M13 2c-5 6-5 16 0 22M13 2c5 6 5 16 0 22" fill="none" stroke="#fff" stroke-width="1.5"/></svg>
      <span><strong>Digital Plan-room</strong><small>Nunc tempus felis vitae urna</small></span></a>
  </main>

  <footer>
    <div class="abs footer"></div>
    <div class="abs foot-col" style="left:54px">
      <h3 class="foot-title">Quick Links</h3>
      <ul><li>The KRF Difference</li><li>About</li><li>Sustainability</li><li>Products &amp; Services</li><li>Reprograhics</li><li>Digital File Management</li></ul>
    </div>
    <div class="abs foot-col" style="left:218px">
      <h3 class="foot-title">Sublinks</h3>
      <ul><li>Color Graphics</li><li>Equipment &amp; Supplies</li><li>Login</li><li>Blog</li><li>Contact Us</li></ul>
    </div>
    <div class="abs testimonials">
      <h3>Testimonials</h3>
      <p>Phasellus felis dolor, scelerisque a, tempus eget, lobortis id, libero. Donec scelerisque leo ac risus. Praesent sit amet est. In dictum, dolor eu dictum porttitor, enim felis viverra mi, eget luctus massa purus quis odio.</p>
      <div class="author">By Author Name</div>
      <svg width="24" height="16" viewBox="0 0 24 16"><path d="M8 2L2 8l6 6M16 2l6 6-6 6" fill="none" stroke="#fff" stroke-width="1.6"/></svg>
    </div>
    <h3 class="abs foot-title" style="left:656px;top:956px">Get Connected</h3>
    <div class="abs social"><i></i><i></i><i></i></div>
    <div class="abs social-names">QN &nbsp;/ Chirpo / WorkLoop</div>
    <div class="abs foot-rule"></div>
    <div class="abs copyright">© 2013 Company Name. &nbsp;All right reserved. &nbsp;Term of Use</div>
  </footer>
</div>
</body>
</html>
```